[Green Press + Juice Bar] Digital Menu Boards (2)

We need designs for our digital menu screens. Dimensions are 1080 x 1920 (9:16). Screens are in portrait mode–2 of them. They will be side by side so designs should be cohesive. We'll need the (Adobe) source files to be able to easily edit in the future.

Check out our Instagram (@pulpwell) to see current brand imagery for inspiration. Please disregard our current website design as it shows our old branding. Visit our Tastemap page to get a feel of the store flow in which the menu boards will be displayed: https://www.tastemap.example/biz/pulpwell-chicago-6

See "Larkfield Menu" attachment for content that will be incorporated into the design for 2 screens.

See "Cleanse Brochure" attachment to see current material we are using to promote our cleansing program. We would like to designate a portion of our menu to promote cleanse options, depending on how much room is available.

Also attached is a photo of our current, static menu board.

We've attached photos of color palettes we like.

Target Market(s)

Health-conscious individuals, healthy moms, fitness gurus, professionals

Industry/Entity Type

Health And Wellness

Font styles to use
Serif
Sans Serif

Colors

Designer to choose colors to be used in the design.

Requirements
Must have
• We need designs for our digital menu screens. Dimensions are 1080 x 1920 (9:16). Screens are in portrait mode–2 of them. We'll need the (Adobe) source files to be able to easily edit in the future. To ensure the sizing of the outputted file is correct and spaced correctly, send us a test file to test on our TV.
Nice to have
• Ideally, the menu will reflect current branding with font usage of one or more of the following:
• FuturaStd-Bold
• Desiderata-Regular
• Wisdom Script
• Bernier Typeface
• Swistblnk Banthers
• Hanley
• If there is space, we'd like to have space to roll a photo/video slideshow on the menu.

```html
<!DOCTYPE html>
<html lang="en">
<head>
<meta charset="utf-8">
<title>Green Press + Juice Bar — Larkfield Menu</title>
<link href="https://fonts.googleapis.com/css2?family=Lobster&family=Oswald:wght@500;600&family=Pathway+Gothic+One&display=swap" rel="stylesheet">
<style>
  :root {
    --board-green: #8dd65a;
    --tag-pink: #c93a6b;
    --price-yellow: #f5e34a;
    --ink: #111111;
    --white: #ffffff;
  }
  * { margin: 0; padding: 0; box-sizing: border-box; }
  html, body { width: 676px; height: 1200px; overflow: hidden; }
  body { background: var(--board-green); }
  .menu-board {
    position: relative; width: 676px; height: 1200px;
    background: var(--board-green); color: var(--ink);
    font-family: "Pathway Gothic One", "Arial Narrow", sans-serif;
  }
  .column-divider {
    position: absolute; left: 382px; top: 30px; width: 2px; height: 1140px;
    background: var(--white);
  }
  .section-title {
    position: absolute; font-family: "Lobster", cursive;
    font-size: 62px; line-height: 1; color: var(--white); font-weight: 400;
  }
  .section-title .size-note { font-family: "Oswald", sans-serif; font-size: 24px; font-weight: 500; }
  .bowl { position: absolute; left: 36px; width: 326px; }
  .bowl-name {
    display: inline-block; background: var(--tag-pink); color: var(--white);
    font-family: "Oswald", sans-serif; font-weight: 600; font-size: 20px;
    line-height: 30px; padding: 0 8px; letter-spacing: 0.3px;
  }
  .bowl-price {
    font-family: "Oswald", sans-serif; font-weight: 500; font-size: 19px;
    color: var(--price-yellow); margin-left: 8px; vertical-align: top; line-height: 30px;
  }
  .bowl-details {
    font-size: 14.5px; line-height: 21.6px; text-transform: uppercase; margin-top: 4px;
  }
  .label { color: var(--white); }
  .build-box {
    position: absolute; left: 40px; top: 876px; width: 312px; height: 308px;
    background: var(--tag-pink); color: var(--white); padding: 14px 24px;
  }
  .build-title { font-family: "Lobster", cursive; font-size: 34px; line-height: 36px; font-weight: 400; }
  .build-title .price { font-family: "Oswald", sans-serif; font-size: 22px; color: var(--price-yellow); }
  .build-steps { list-style: none; margin-top: 12px; font-size: 15.5px; line-height: 22px; text-transform: uppercase; }
  .build-steps li { margin-bottom: 4px; }
  .item { position: absolute; left: 410px; width: 250px; }
  .item-name {
    font-family: "Oswald", sans-serif; font-weight: 500; font-size: 19px;
    line-height: 27px; color: var(--white); text-transform: uppercase;
  }
  .item-price, .item-note { font-size: 14px; color: var(--price-yellow); font-family: "Oswald", sans-serif; font-weight: 500; }
  .item-note { display: block; line-height: 18px; }
  .item-desc { font-size: 14.5px; line-height: 21.6px; text-transform: uppercase; margin-top: 4px; }
  .divider-rule { position: absolute; left: 414px; top: 954px; width: 202px; height: 2px; background: var(--white); }
  .cleanse-notes { font-size: 11px; line-height: 16px; text-transform: uppercase; margin-top: 14px; }
</style>
</head>
<body>
<main class="menu-board">
  <div class="column-divider"></div>

  <h1 class="section-title" style="left:36px;top:14px;">Bowls <span class="size-note">(20oz)</span></h1>

  <section class="bowl" style="top:104px;">
    <span class="bowl-name">MATCHA BOWL</span><span class="bowl-price">12.5</span>
    <p class="bowl-details"><span class="label">Base:</span> fresh-cracked coconut water, coconut meat, banana, spinach, medjool dates, tocotrienols, maca, matcha, spirulina. <span class="label">Toppings:</span> hemp seeds, blueberries, cacao nibs, coconut shreds, kiwi, pomegranate seeds, banana, bee pollen, mint sprig.</p>
  </section>

  <section class="bowl" style="top:298px;">
    <span class="bowl-name">FRUIT ALCHEMIST</span><span class="bowl-price">12</span>
    <p class="bowl-details"><span class="label">Base:</span> acai, fresh-pressed apple juice, cherries, banana, strawberry, pomegranate, <span class="label">Toppings:</span> seasonal berries, banana, sprouted almond butter, coconut shreds, goji berries, bee pollen, housemade coconut whip, housemade raw granola, local honey.</p>
  </section>

  <section class="bowl" style="top:490px;">
    <span class="bowl-name">HARLEQUIN MONKEY</span><span class="bowl-price">12</span>
    <p class="bowl-details"><span class="label">Base:</span> acai, housemade almond milk, bananas, blueberries, peanut butter, medjool dates <span class="label">Toppings:</span> housemade raw granola, raw chocolate hearts, peanut butter, raw cacao drizzle, banana, dried banana chips, cacao nibs, local honey, bee pollen.</p>
  </section>

  <section class="bowl" style="top:686px;">
    <span class="bowl-name">KETO BOWL</span><span class="bowl-price">13 (UNDER</span>
    <div class="bowl-price" style="margin-left:0;line-height:26px;display:block;">15 NET CARBS)</div>
    <p class="bowl-details" style="margin-top:2px;"><span class="label">Base:</span> acai, housemade almond milk, coconut meat, avocado, blueberries, cauliflower, pineapple, sprouted almond butter, xylitol. <span class="label">Toppings:</span> seasonal berries, coconut shreds, bee pollen, hemp seeds, mulberries, chia seeds.</p>
  </section>

  <section class="build-box">
    <h2 class="build-title">Build Your<br>Own Bowl <span class="price">- $12.5</span></h2>
    <ol class="build-steps">
      <li>Step 1: Start with your liquid- almond milk, apple juice, coconut water</li>
      <li>Step 2: Choose up to 2 fruits/veggies (all bowls include banana)</li>
      <li>Step 3: Choose up to 2 superfood add-ins</li>
      <li>Step 4: Choose up to 4 superfood toppings</li>
      <li>Step 5: Choose a sweetener (medjool dates, local honey, xylitol)</li>
    </ol>
  </section>

  <h1 class="section-title" style="left:410px;top:26px;">Bites</h1>

  <section class="item" style="top:102px;">
    <h3 class="item-name">Hot oatmeal +<br>seasonal fruit<br>+ superfood toppings <span class="item-price">7.5</span></h3>
    <p class="item-desc">(Served until 10:30am).</p>
  </section>

  <section class="item" style="top:234px;">
    <h3 class="item-name">Avocado toast</h3>
    <span class="item-note">(2 slices 8.5/1 slice 4.5)</span>
    <p class="item-desc">Sprouted Harvest 7 bread, avocado, pomegranate, fig, rosemary.</p>
  </section>

  <section class="item" style="top:346px;">
    <h3 class="item-name">Orange cacao toast</h3>
    <span class="item-note">(2 slices 8.5/<br>1 slice 4.5) *seasonal*</span>
    <p class="item-desc">Sprouted Harvest 7 cinnamon raisin bread, sprouted almond butter, orange, cacao nibs, local honey, basil.</p>
  </section>

  <h1 class="section-title" style="left:410px;top:536px;">Soups</h1>

  <section class="item" style="top:608px;">
    <h3 class="item-name">Broccoli “cheddar” soup</h3>
    <span class="item-note">16oz (dairy free)</span>
    <p class="item-desc">Red pepper, carrot, cashew, spring onion, lemon, maple, nutritional yeast, pink salt, chili powder, garlic powder, broccoli.</p>
  </section>

  <section class="item" style="top:744px;">
    <h3 class="item-name">Veggie soup with<br>sprouted lentil <span class="item-price">16oz</span></h3>
    <p class="item-desc">Leek, kale, celery, red pepper, green onion, liquid aminos, fresh ginger, fresh garlic, lemon, salt, pepper, cumin, turmeric, sprouted lentils.</p>
  </section>

  <div class="divider-rule"></div>

  <section class="item" style="top:1000px;">
    <h3 class="item-name">Signature juice and<br>smoothie cleanses</h3>
    <p class="cleanse-notes">*Available at 65/day with nationwide delivery available.<br>*Choose from 5 different signature cleanses available in 1, 3, 5 or 7 day packages<br>*Reboot your body by providing a digestive vacation while refocusing the mind</p>
  </section>
</main>
</body>
</html>
```